Financial PR company Homepage and Inner Page design

Please design a web homepage and innerpage for LORVIA Public Relations.
LORVIA Public Relations is a Financial PR company targeting Shenzhen Qian Special Economical Zone.
Note:
1. Menu includes ( Please specialize in Chinese and we want to see the Chinese fonts)
关于我们/服务板块/专业优势/合作伙伴/前海商圈/公司新闻/加盟我们/联系我们

2. Please refer to world class PR Business company and contribute your idea on website design and color themes.

3. We have attached the Logo for reference.

4. Anytime use picture for reference, please select asian business people pictures.

Cheers,

HI Designers, Thanks for the design submission. Here is our client feedback: 1. Adopt one screen design. 2. Use amiable Asia Business woman pictures. 3. Use contrastive color theme for the design. Cheers, Kit From PW

```html
<!DOCTYPE html>
<html lang="zh-CN">
<head>
<meta charset="utf-8">
<title>LORVIA Public Relations</title>
<link rel="stylesheet" href="https://fonts.googleapis.com/css2?family=Open+Sans:wght@400;600;700&family=Arimo:wght@400;700&family=Noto+Sans+SC:wght@400;700&display=swap">
<style>
  :root {
    --navy: #0f1f33;
    --accent: #0b9be2;
    --white: #ffffff;
    --page-bg: #dedede;
    --card-inner: #f2f2f2;
    --ink: #111111;
    --title-ink: #333333;
    --footer-top: #9a9a9a;
    --footer-bottom: #7a7a7a;
  }
  * { margin: 0; padding: 0; box-sizing: border-box; }
  html, body { width: 1200px; height: 1003px; overflow: hidden; }
  body {
    position: relative;
    background: var(--page-bg);
    font-family: "Arimo", "Noto Sans SC", Arial, sans-serif;
    color: var(--ink);
  }

  /* Header */
  .site-header {
    position: absolute; left: 0; top: 0; width: 1200px; height: 91px;
    background: linear-gradient(#0c1a2b, var(--navy) 60%, #132842);
  }
  .brand { position: absolute; left: 138px; top: 24px; display: flex; align-items: center; gap: 12px; text-decoration: none; }
  .brand-mark { width: 16px; height: 16px; border-radius: 50%; background: var(--accent); }
  .brand-name {
    font-family: "Open Sans", sans-serif; font-size: 34px; font-weight: 400;
    line-height: 40px; letter-spacing: 1px; color: var(--white);
  }

  .main-nav { position: absolute; left: 397px; top: 0; height: 91px; display: flex; align-items: center; }
  .main-nav a, .footer-nav a {
    font-family: "Noto Sans SC", sans-serif; font-weight: 700; font-size: 11.5px;
    color: var(--white); text-decoration: none;
  }
  .main-nav .is-active {
    display: flex; align-items: center; justify-content: center;
    width: 52px; height: 91px; background: var(--accent); margin-right: 15px;
  }
  .nav-sep { color: var(--white); font-size: 11.5px; margin: 0 8px; font-weight: 700; }

  .client-area {
    position: absolute; left: 970px; top: 0; width: 111px; height: 21px;
    background: linear-gradient(#ffffff, #e4e4e4); border-radius: 0 0 4px 4px;
    font-family: "Open Sans", sans-serif; font-size: 13px; color: #333; text-decoration: none;
    display: flex; align-items: center; justify-content: center;
  }

  /* Hero */
  .hero { position: absolute; left: 0; top: 91px; width: 1200px; height: 397px; }
  .hero-photo {
    position: absolute; inset: 0;
    background:
      radial-gradient(ellipse 420px 200px at 300px 330px, rgba(214,150,70,0.55), transparent 70%),
      radial-gradient(ellipse 500px 260px at 760px 300px, rgba(190,120,50,0.45), transparent 70%),
      linear-gradient(180deg, #2a4a80 0%, #3e5f92 30%, #4a4f5c 60%, #3a2c22 100%);
  }
  .hero-arrow {
    position: absolute; top: 168px; width: 44px; height: 44px;
    display: flex; align-items: center; justify-content: center;
  }
  .hero-arrow.prev { left: 147px; }
  .hero-arrow.next { left: 1009px; border-radius: 50%; background: rgba(255,255,255,0.12); }
  .hero-caption {
    position: absolute; left: 555px; top: 299px; width: 290px; height: 60px;
    background: rgba(20,20,20,0.45);
    display: flex; align-items: center; padding-left: 20px;
    font-family: "Noto Sans SC", sans-serif; font-size: 31px; color: var(--white);
    letter-spacing: 1px; text-shadow: 0 1px 3px rgba(0,0,0,0.8);
  }

  /* Feature band */
  .features { position: absolute; left: 0; top: 488px; width: 1200px; height: 108px; display: flex; }
  .feature { position: relative; height: 108px; color: var(--white); }
  .feature-dark { background: linear-gradient(100deg, #15273f, #1d3552 60%, #13243a); }
  .feature-dark.team { background: linear-gradient(100deg, #2a2d33, #3a3d44 60%, #25282d); }
  .feature-active { background: var(--accent); }
  .feature-icon { position: absolute; }
  .feature h2 {
    position: absolute; font-family: "Open Sans", sans-serif; font-weight: 700;
    font-size: 15px; top: 17px; letter-spacing: 0.2px;
  }
  .feature p { position: absolute; top: 43px; width: 200px; font-size: 11.3px; line-height: 15.5px; }

  /* Welcome card */
  .welcome-shadow {
    position: absolute; left: 170px; top: 880px; width: 870px; height: 22px;
    background: radial-gradient(ellipse at 50% 0%, rgba(0,0,0,0.35), transparent 70%);
  }
  .welcome-card {
    position: absolute; left: 131px; top: 636px; width: 937px; height: 250px;
    background: var(--white); border-radius: 8px; padding: 9px;
  }
  .welcome-inner {
    position: relative; width: 100%; height: 100%; background: var(--card-inner); border-radius: 6px;
  }
  .welcome-inner h1 {
    position: absolute; left: 9px; top: 19px; font-family: "Arimo", sans-serif;
    font-weight: 400; font-size: 19px; color: var(--title-ink);
  }
  .welcome-copy {
    position: absolute; left: 9px; top: 56px; width: 620px;
    font-size: 11.2px; line-height: 20.6px; letter-spacing: 0.75px; white-space: nowrap;
  }
  .welcome-copy p + p { margin-top: 20.6px; }
  .welcome-photo {
    position: absolute; left: 630px; top: 62px; width: 278px; height: 130px;
    background: linear-gradient(180deg, #7a2d5a 0%, #3b3350 25%, #4a5a55 60%, #202a2e 100%);
    border: 1px solid #cfcfcf;
  }

  /* Footer */
  .site-footer {
    position: absolute; left: 0; top: 931px; width: 1200px; height: 72px;
    background: linear-gradient(var(--footer-top), var(--footer-bottom));
  }
  .footer-nav { position: absolute; left: 145px; top: 13px; display: flex; align-items: center; }
  .footer-nav a { font-size: 11px; }
  .footer-nav .nav-sep { font-size: 11px; margin: 0 7px; }
  .footer-nav .first { margin-right: 16px; }
  .copyright { position: absolute; left: 145px; top: 40px; font-size: 11.5px; color: var(--white); }
</style>
</head>
<body>
  <header class="site-header">
    <a class="brand" href="#">
      <span class="brand-mark"></span>
      <span class="brand-name">LORVIA</span>
    </a>
    <nav class="main-nav">
      <a class="is-active" href="#">关于我们</a>
      <a href="#">服务板块</a><span class="nav-sep">/</span>
      <a href="#">专业优势</a><span class="nav-sep">/</span>
      <a href="#">合作伙伴</a><span class="nav-sep">/</span>
      <a href="#">前海商圈</a><span class="nav-sep">/</span>
      <a href="#">公司新闻</a><span class="nav-sep">/</span>
      <a href="#">加盟我们</a><span class="nav-sep">/</span>
      <a href="#">联系我们</a>
    </nav>
    <a class="client-area" href="#">Client Area</a>
  </header>

  <section class="hero">
    <div class="hero-photo" role="img" aria-label="City skyline at dusk with a lit suspension bridge"></div>
    <span class="hero-arrow prev">
      <svg width="20" height="30" viewBox="0 0 20 30"><path d="M15 3 L5 15 L15 27" fill="none" stroke="rgba(255,255,255,0.8)" stroke-width="4"/></svg>
    </span>
    <span class="hero-arrow next">
      <svg width="20" height="30" viewBox="0 0 20 30"><path d="M5 3 L15 15 L5 27" fill="none" stroke="rgba(255,255,255,0.9)" stroke-width="4"/></svg>
    </span>
    <div class="hero-caption">简单是终极的复杂</div>
  </section>

  <section class="features">
    <div class="feature feature-dark" style="width:452px">
      <svg class="feature-icon" style="left:151px;top:37px" width="68" height="50" viewBox="0 0 68 50">
        <g fill="none" stroke="#fff" stroke-width="3">
          <path d="M2 50 V26 H10"/><path d="M16 50 V4 H36 V50"/><path d="M42 50 V18 H54 V36 H66 V50"/>
        </g>
        <g fill="#fff"><rect x="22" y="12" width="4" height="5"/><rect x="28" y="12" width="4" height="5"/><rect x="22" y="22" width="4" height="5"/><rect x="46" y="24" width="4" height="4"/></g>
      </svg>
      <h2 style="left:231px">ABOUT US</h2>
      <p style="left:231px">Lorem Ipsum is simply dummy text of printing and typesetting indus Lorem Ipsum has been the standa</p>
    </div>
    <div class="feature feature-active" style="width:304px">
      <svg class="feature-icon" style="left:31px;top:38px" width="40" height="52" viewBox="0 0 40 52">
        <path fill="#fff" d="M6 0 H12 V5 H17 V0 H23 V5 H28 V0 H34 V12 H6 Z M10 15 H30 L34 42 H6 Z M2 45 H38 V52 H2 Z"/>
        <rect x="14" y="20" width="5" height="16" fill="#0b9be2"/>
      </svg>
      <h2 style="left:93px">OUR STRATEGY</h2>
      <p style="left:93px">Lorem Ipsum is simply dummy text of printing and typesetting indus Lorem Ipsum has been the standa</p>
    </div>
    <div class="feature feature-dark team" style="width:444px">
      <svg class="feature-icon" style="left:20px;top:45px" width="66" height="44" viewBox="0 0 66 44">
        <g fill="#fff">
          <circle cx="14" cy="10" r="7"/><circle cx="33" cy="8" r="8"/><circle cx="52" cy="10" r="7"/>
          <path d="M2 44 V30 Q2 20 14 20 Q22 20 24 26 V44 Z"/>
          <path d="M42 44 V26 Q44 20 52 20 Q64 20 64 30 V44 Z"/>
          <path d="M20 44 V30 Q20 18 33 18 Q46 18 46 30 V44 Z"/>
        </g>
      </svg>
      <h2 style="left:95px">MEET THE TEAM</h2>
      <p style="left:95px">Lorem Ipsum is simply dummy text of printing and typesetting indus Lorem Ipsum has been the standa</p>
    </div>
  </section>

  <div class="welcome-shadow"></div>
  <main class="welcome-card">
    <div class="welcome-inner">
      <h1>Welcome to LORVIA Public Relations</h1>
      <div class="welcome-copy">
        <p>Lorem ipsum dolor sit amet, consectetur adipiscing elit. Proin pulvinar eros in imperdiet porttitor. Praesent<br>velit justo, placerat ut ornare aliquet, venenatis vel justo. Nulla porttitor enim vitae nibh scelerisque, nec<br>laoreet libero posuere. Integer ut neque ut purus dictum auctor. Cras tincidunt odio a pharetra iaculis.<br>Nam in arcu eu tortor consequat tempor. Vivamus eu convallis risus.</p>
        <p>Mauris pulvinar, eros ac elementum tempus, enim metus vehicula ante, ut scelerisque ipsum libero non<br>sem. Integer a commodo augue. Ut accumsan efficitur mattis. Donec ut mollis nisl. Suspendisse tincidunt</p>
      </div>
      <div class="welcome-photo" role="img" aria-label="Classical stone columns of a financial building lit at night"></div>
    </div>
  </main>

  <footer class="site-footer">
    <nav class="footer-nav">
      <a class="first" href="#">关于我们</a>
      <a href="#">服务板块</a><span class="nav-sep">/</span>
      <a href="#">专业优势</a><span class="nav-sep">/</span>
      <a href="#">合作伙伴</a><span class="nav-sep">/</span>
      <a href="#">前海商圈</a><span class="nav-sep">/</span>
      <a href="#">公司新闻</a><span class="nav-sep">/</span>
      <a href="#">加盟我们</a><span class="nav-sep">/</span>
      <a href="#">联系我们</a>
    </nav>
    <p class="copyright">Copyright © 2014 - &nbsp;LORVIA Public Relations - All rights reserved.</p>
  </footer>
</body>
</html>
```